Vitamin B12 Liquid Drops Label

hi, i need a label designed for my vitamin b12 drops that i am going to be selling on bazaarly. the label needs to quickly capture the attention of a buyer as he or she is scrolling through the thumbnail search results on bazaarly.net my brand is called zulmo. i already have an example brand logo i will be using, however, i need help designing the rest of the label. attached are some examples of labels i like for other supplements.some of these examples are pink. i do not want pink. please go for a blue/green color scheme. THE DESIGN MUST BE BOLD

Target Market(s)

adults ages 30 - 64

Font styles to use
Sans Serif

Colors
0455a3
cedeed
3176b5
85acd3
cfdeed
9bcb3b
abd037
cadf82
00a990

Requirements
Must have
• - bold design
• - somewhat gender-neutral color scheme because this will be used equally by men and women
• - B12 MUST be very prominent and visible on the label
Should not have
• - it should not be "crunchy" looking

```html
<!DOCTYPE html>
<html lang="en">
<head>
<meta charset="utf-8">
<title>Vitamin B12 Oral Drops Label</title>
<link rel="stylesheet" href="https://fonts.googleapis.com/css2?family=Open+Sans:wght@400;600;700;800&display=swap">
<style>
  :root {
    --backdrop: #ececec;
    --label-white: #f7f8f8;
    --ink: #2c2f33;
    --green: #9bcb3b;
    --green-soft: #cadf82;
    --teal: #00a990;
    --blue: #3176b5;
    --blue-soft: #85acd3;
    --blue-pale: #cedeed;
    --white: #ffffff;
  }
  * { box-sizing: border-box; margin: 0; padding: 0; }
  html, body {
    width: 1200px;
    height: 857px;
    overflow: hidden;
    background: var(--backdrop);
    font-family: "Open Sans", Arial, sans-serif;
  }
  .canvas {
    position: relative;
    width: 1200px;
    height: 857px;
  }
  .label {
    position: absolute;
    left: 420px;
    top: 24px;
    width: 360px;
    height: 808px;
    background: var(--label-white);
    overflow: hidden;
    box-shadow: 0 2px 10px rgba(0,0,0,0.08);
  }
  .label__pattern {
    position: absolute;
    left: 0;
    right: 0;
    top: 380px;
    bottom: 0;
    background: linear-gradient(180deg,
      rgba(247,248,248,0) 0%,
      rgba(202,223,130,0.45) 30%,
      rgba(155,203,59,0.35) 55%,
      rgba(133,172,211,0.75) 85%,
      var(--blue-soft) 100%);
  }
  .label__format {
    position: absolute;
    top: 30px;
    right: 26px;
    font-size: 19px;
    font-weight: 400;
    line-height: 1;
    color: var(--ink);
  }
  .label__band {
    position: absolute;
    left: 0;
    right: 0;
    top: 152px;
    height: 72px;
    background: linear-gradient(90deg, var(--green-soft) 0%, var(--green) 30%, var(--teal) 75%, #7cc9a8 100%);
    opacity: 0.9;
    display: flex;
    align-items: center;
    justify-content: center;
  }
  .label__band-text {
    color: var(--white);
    font-size: 36px;
    font-weight: 800;
    letter-spacing: 3px;
    line-height: 1;
  }
  .label__vitamin {
    position: absolute;
    left: 0;
    right: 0;
    top: 300px;
    text-align: center;
    font-size: 120px;
    font-weight: 800;
    line-height: 1;
    letter-spacing: -2px;
    color: var(--teal);
  }
  .label__volume {
    position: absolute;
    right: 26px;
    bottom: 38px;
    font-size: 27px;
    font-weight: 400;
    line-height: 1;
    color: var(--ink);
  }
</style>
</head>
<body>
<div class="canvas">
  <section class="label">
    <div class="label__pattern" role="img" aria-label="Soft field of translucent green and blue hexagon shapes"></div>
    <p class="label__format">Oral drops</p>
    <div class="label__band"><span class="label__band-text">VITAMIN</span></div>
    <p class="label__vitamin">B12</p>
    <p class="label__volume">50 ml</p>
  </section>
</div>
</body>
</html>
```